MOLVIKAN Hemp based Pet Brand that growns it's own premium hemp and creates amazing pet products.

We need packaging designed for a new company based in South West Florida. We grow our own hemp with our other company Fern 9 Vat and use the harvest to make our hemp based pet products. Our initial products are pet treats that include Soft Chews and Calming Chews. The bags come in two different sizes. Regular bag being 7x10.25 inches and Small bag 4.25X6.25 inches. We also need a tincture box and label created. We want packaging that will catch the eye of the consumer and colors that compliment our logo. Dropper label size is 4x1.75 inches and the milligram of CBD is 1500. We have attached our manufacturers packaging and would like you to coppy everything other than their overall design and logo. Use default UPC and QR code, which we can replace later in the Ai file. Please see all the attached documents and please ask me if you have any questions. The final design should communicate a premium product that stand our from the rest. Something that catches the eye of the consumer by its premium appearance. Packaging is everything so I hope you can use your creative skills to create something special!

Target Market(s)

Pet owners

Font styles to use
Serif
Sans Serif

Colors
0054AA
0677BA
7BADD7
CADEEF
E8F1F8
0094D4
00A9DD
6FCCEA
C7EBF8
E9F6FB
EE7325
F08F49
F5BC92
FAE3D3
FDF4ED

Requirements
Must have
• Stand out design. Premium feel. Imagine shopping for something for your pet and seeing a brand that POPS and just looks like a good product because the packaging is so good.
Nice to have
• Modern mature feel
Should not have
• Cartoony feeling. Do not use baby blue everywhere. Do not include pictures of people in the packaging

```html
<!DOCTYPE html>
<html lang="en">
<head>
<meta charset="utf-8">
<title>MOLVIKAN Soft Chews Pouch</title>
<link href="https://fonts.googleapis.com/css2?family=Bebas+Neue&family=Montserrat:wght@500;700&display=swap" rel="stylesheet">
<style>
  :root {
    --stage: #1b7c98;
    --teal-light: #4fc0c8;
    --teal-mid: #2a9fc4;
    --blue-deep: #1f6fae;
    --orange-soft: #e9833f;
    --logo-fill: #6fccea;
    --ink: #2b2b2b;
    --white: #ffffff;
    --ribbon: #d42a2a;
    --cream-1: #efe6cf;
    --cream-2: #d9c9a4;
    --gold: #c9a24a;
  }
  html, body { margin: 0; padding: 0; overflow: hidden; }
  body {
    width: 1200px; height: 1200px;
    background: var(--stage);
    position: relative;
    font-family: "Montserrat", sans-serif;
  }
  .pouch {
    position: absolute; left: 267px; top: 50px;
    width: 665px; height: 1100px;
    background: linear-gradient(200deg, var(--teal-light) 0%, var(--teal-mid) 45%, var(--blue-deep) 100%);
    overflow: hidden;
  }
  .orange-band {
    position: absolute; left: 55px; top: 0;
    width: 236px; height: 494px;
    background: var(--orange-soft);
  }
  .seal-line {
    position: absolute; left: 0; width: 100%; height: 3px;
    background: rgba(255,255,255,0.25);
  }
  .seal-line.top { top: 94px; }
  .seal-line.zip { top: 181px; }
  .dog-photo {
    position: absolute; left: 0; top: 0;
    width: 665px; height: 1100px;
  }
  .brand-seal {
    position: absolute; left: 70px; top: 382px;
    width: 212px; height: 212px; border-radius: 50%;
    background: var(--orange-soft);
    display: flex; align-items: center; justify-content: center;
  }
  .brand-seal-inner {
    width: 192px; height: 192px; border-radius: 50%;
    background: var(--logo-fill);
    display: flex; align-items: center; justify-content: center;
  }
  .brand-name {
    font-family: "Bebas Neue", sans-serif;
    font-size: 40px; letter-spacing: 3px;
    color: var(--ink);
  }
  .title {
    position: absolute; left: 92px; top: 626px;
    font-family: "Bebas Neue", sans-serif;
    line-height: 0.86; margin: 0; font-weight: 400;
  }
  .title .soft { display: block; font-size: 72px; color: var(--ink); }
  .title .chews { display: block; font-size: 132px; color: var(--white); letter-spacing: -1px; }
  .quality-badge {
    position: absolute; left: 450px; top: 926px;
    width: 84px; height: 84px; border-radius: 50%;
    background: radial-gradient(circle, #2a2a2a 58%, var(--gold) 60%);
  }
  .info-panel {
    position: absolute; left: 71px; top: 826px;
    width: 217px; height: 274px;
    background: var(--orange-soft);
    border-radius: 108px 108px 0 0;
    box-sizing: border-box;
    padding: 32px 14px 0;
  }
  .origin-ribbon {
    display: block; width: 118px; margin: 0 auto;
    background: var(--ribbon); color: var(--white);
    font-size: 7.5px; font-weight: 700; text-align: center;
    padding: 3px 0; transform: rotate(3deg);
  }
  .rule { border: 0; border-top: 1px solid var(--ink); margin: 12px 0 6px; }
  .description {
    font-size: 6.6px; line-height: 1.95; color: var(--ink); margin: 0;
    transform: rotate(3deg);
  }
  .info-footer {
    display: flex; align-items: center; gap: 14px; margin-top: 12px; padding-left: 12px;
  }
  .claim-icon { width: 30px; height: 30px; }
  .net {
    font-family: "Bebas Neue", sans-serif;
    font-size: 9.5px; line-height: 1.3; color: var(--ink);
  }
</style>
</head>
<body>
  <div class="pouch">
    <div class="orange-band"></div>
    <div class="seal-line top"></div>
    <div class="seal-line zip"></div>

    <svg class="dog-photo" viewBox="0 0 665 1100" role="img" aria-label="Photo of a smiling yellow Labrador puppy with an orange collar, sitting and looking up to the left">
      <defs>
        <linearGradient id="dogTone" x1="0" y1="0" x2="0.3" y2="1">
          <stop offset="0" stop-color="#efe6cf"/>
          <stop offset="1" stop-color="#d9c9a4"/>
        </linearGradient>
      </defs>
      <path d="M332 440 C330 410 372 392 420 391 C500 388 600 410 642 470 L642 1100 L340 1100 C345 1030 370 950 400 880 C430 820 470 760 482 716 C440 640 390 610 350 588 C330 560 328 490 332 440 Z" fill="url(#dogTone)"/>
    </svg>

    <div class="brand-seal">
      <div class="brand-seal-inner"><span class="brand-name">MOLVIKAN</span></div>
    </div>

    <h1 class="title"><span class="soft">Soft</span><span class="chews">Chews</span></h1>

    <div class="quality-badge" role="img" aria-label="Quality badge"></div>

    <div class="info-panel">
      <span class="origin-ribbon">South West Florida</span>
      <hr class="rule">
      <p class="description">Our canine soft chews are a vital part of your dogs daily health and nutrition. Our proprietary blend of organic hemp, with naturally occurring CBDa, provides the most effective way to supplement the health and wellness of your pet. Pain, inflammation, anxiety, skin/coat health and restfulness are important to a dog's overall health.</p>
      <div class="info-footer">
        <svg class="claim-icon" viewBox="0 0 30 30" role="img" aria-label="Vegan mark"><circle cx="15" cy="15" r="13" fill="none" stroke="#2b2b2b" stroke-width="1.5"/></svg>
        <svg class="claim-icon" viewBox="0 0 30 30" role="img" aria-label="Grain free mark"><circle cx="15" cy="15" r="13" fill="none" stroke="#2b2b2b" stroke-width="1.5"/><line x1="6" y1="6" x2="24" y2="24" stroke="#2b2b2b" stroke-width="1.5"/></svg>
        <div class="net">Net Ct. 10<br>Net Wt. 2 oz</div>
      </div>
    </div>
  </div>
</body>
</html>
```